Attorney business card for two offices

Looking for a new business card design that can list both of my offices, one in Houston and one in West Texas. Want something masculine, easy to read, and conservative yet somewhat modern. Our current card has used a nautical star on it for years, but I am not necessarily attached to that. Also, a lot of our forms use dark green and orange. Second office address is P.O. Box 518, Redmesa, Texas 79617

```html
<!DOCTYPE html>
<html lang="en">
<head>
<meta charset="utf-8">
<title>Hale Legal Group – Business Card</title>
<link href="https://fonts.googleapis.com/css2?family=Open+Sans:ital,wght@0,400;0,600;1,400&display=swap" rel="stylesheet">
<style>
  :root {
    --orange: #f05a28;
    --ink: #3a3a3a;
    --muted: #6b6b6b;
    --paper: #ffffff;
    --black: #0c0c0c;
    --backdrop: #e9e9e9;
  }
  * { box-sizing: border-box; margin: 0; padding: 0; }
  html, body { width: 1200px; height: 1200px; overflow: hidden; }
  body {
    background: var(--backdrop);
    font-family: "Open Sans", Arial, sans-serif;
    display: flex;
    flex-direction: column;
    align-items: center;
    justify-content: center;
    gap: 60px;
  }
  .card {
    position: relative;
    width: 700px;
    height: 400px;
    overflow: hidden;
    box-shadow: 0 6px 20px rgba(0,0,0,0.12);
  }

  /* Front */
  .card--front { background: var(--paper); color: var(--ink); }
  .attorney { position: absolute; left: 56px; top: 44px; }
  .attorney__name {
    color: var(--orange);
    font-size: 24px;
    font-weight: 400;
    letter-spacing: 0.5px;
  }
  .attorney__title { font-style: italic; font-size: 15px; color: var(--muted); margin-top: 2px; }
  .office { font-size: 15px; line-height: 1.35; margin-top: 12px; }
  .contact {
    display: flex;
    gap: 14px;
    margin-top: 6px;
    font-size: 15px;
    line-height: 1.35;
  }
  .contact__divider { width: 1px; align-self: stretch; background: #9a9a9a; }
  .contact b { font-weight: 600; }
  .houston-office {
    display: inline-block;
    margin-top: 8px;
    background: var(--orange);
    color: var(--paper);
    font-size: 14px;
    padding: 2px 10px;
  }
  .service-band {
    position: absolute;
    left: 0;
    top: 300px;
    width: 440px;
    height: 28px;
    background: var(--orange);
    color: var(--paper);
    font-size: 14px;
    letter-spacing: 3px;
    line-height: 28px;
    padding-left: 40px;
    white-space: nowrap;
  }
  .service-band--end {
    position: absolute;
    left: 468px;
    top: 300px;
    width: 232px;
    height: 28px;
    background: var(--orange);
  }
  .firm-name {
    position: absolute;
    right: 56px;
    top: 166px;
    color: var(--orange);
    font-size: 28px;
    font-weight: 400;
    line-height: 1;
    white-space: nowrap;
  }
  .edge-mark {
    position: absolute;
    right: 24px;
    top: 150px;
    width: 14px;
    height: 70px;
    background: var(--orange);
  }

  /* Back */
  .card--back {
    background: radial-gradient(circle at 40% 30%, #1a1a1a, var(--black) 70%);
    display: flex;
    align-items: center;
    justify-content: center;
    gap: 18px;
  }
  .back-mark { width: 22px; height: 22px; background: var(--orange); }
  .back-name {
    color: var(--orange);
    font-size: 44px;
    font-weight: 400;
    letter-spacing: 1px;
    line-height: 1;
  }
</style>
</head>
<body>
  <section class="card card--front" aria-label="Card front">
    <div class="attorney">
      <h1 class="attorney__name">DANIEL R. HALE, SR.</h1>
      <p class="attorney__title">Attorney of Law</p>
      <p class="office">P.O. Box 518<br>Redmesa, Texas 79617</p>
      <div class="contact">
        <p>T : (713)555-0142<br>F : (832)555-0187</p>
        <span class="contact__divider"></span>
        <p><b>W</b> : www.halelegal.example<br><b>E</b> : daniel@halelegal.example</p>
      </div>
      <p class="houston-office">4810 Cedar Row, suite 210, Larkport texas 77450</p>
    </div>
    <div class="service-band">Power of Attorney and Fee Agreement</div>
    <div class="service-band--end"></div>
    <p class="firm-name">Hale Legal Group</p>
    <div class="edge-mark"></div>
  </section>

  <section class="card card--back" aria-label="Card back">
    <span class="back-mark"></span>
    <p class="back-name">Hale Legal Group</p>
  </section>
</body>
</html>
```